Create a UI design for a cutting edge financial market site
target-audience
We run an on-line cash, futures, and prediction market site. Please see http://quorvatrade.example/ for our current design & site
Description
Mobile friendly, polish, and ease of use

```html
<!DOCTYPE html>
<html lang="en">
<head>
<meta charset="utf-8">
<title>QUORVATRADE – Market</title>
<link rel="stylesheet" href="https://fonts.googleapis.com/css2?family=Oswald:wght@500&family=Open+Sans:wght@400;600;700&display=swap">
<style>
:root{
  --page:#f4f4f4;
  --blue-top:#2e8ee0;
  --blue-bottom:#0f5fb0;
  --ticker:#2f2f2f;
  --white:#ffffff;
  --panel-blue:#0a5fb8;
  --panel-body:#f1f1f1;
  --rule:#c9c9c9;
  --text:#555555;
  --muted:#777777;
  --grid:#e6e6e6;
  --s1:#4f93d8;--s2:#a3a3a3;--s3:#3d6fc4;--s4:#1e4f94;--s5:#5e5e5e;--s6:#1f3770;
}
*{box-sizing:border-box;margin:0;padding:0}
html,body{width:1200px;height:938px;overflow:hidden}
body{background:var(--page);background-image:radial-gradient(#e2e2e2 1px,transparent 1px);background-size:4px 4px;font-family:"Open Sans",Arial,sans-serif;color:var(--text);position:relative}
.site-header{position:absolute;left:100px;top:0;width:1000px;height:57px;background:linear-gradient(var(--blue-top),var(--blue-bottom))}
.brand{position:absolute;left:18px;top:6px;font-family:"Oswald",sans-serif;font-weight:500;font-size:34px;color:var(--white);letter-spacing:-.5px}
.auth-btn{position:absolute;top:16px;height:26px;border:2px solid #7ec2f5;border-radius:5px;background:linear-gradient(#3aa0ee,#1277d4);color:var(--white);font:700 11px "Open Sans",sans-serif;display:flex;align-items:center;justify-content:center}
.auth-btn.register{left:794px;width:90px}
.auth-btn.login{left:899px;width:90px}
.ticker{position:absolute;left:100px;top:57px;width:1000px;height:53px;background:var(--ticker);color:var(--white);font-weight:700;font-size:13px}
.ticker span{position:absolute;top:18px}
.chat-badge{position:absolute;left:918px;top:10px;width:72px;height:34px;border:2px solid #2ca3e8;border-radius:5px;background:var(--white)}
.chart-card{position:absolute;left:100px;top:124px;width:1000px;height:516px;background:var(--white);border:1px solid #e4e4e4}
.chart-card svg{position:absolute;left:0;top:0}
.panel{position:absolute;top:678px;height:188px;background:var(--panel-body)}
.panel h2{height:32px;background:var(--panel-blue);color:var(--white);font-size:15px;font-weight:600;padding:6px 0 0 10px;letter-spacing:.3px}
.panel table{border-collapse:collapse;margin:12px 0 0 8px;font-size:13px}
.panel th{text-align:left;font-weight:600;color:#666;height:24px;border-bottom:1px solid var(--rule);font-size:12.5px}
.panel td{height:29px;border-bottom:1px solid var(--rule);font-weight:700;color:#666}
.panel tr:last-child td{border-bottom:none}
.bids{left:100px;width:302px}
.asks{left:406px;width:322px;box-shadow:-3px 0 4px rgba(0,0,0,.1)}
.trades{left:732px;width:368px;box-shadow:-3px 0 4px rgba(0,0,0,.1)}
.bids h2,.asks h2,.trades h2{padding-left:10px}
.asks h2,.trades h2{padding-left:24px}
.asks table,.trades table{margin-left:24px}
.site-footer{position:absolute;left:100px;top:892px;width:1000px;border-top:1px solid #555;font-size:12.5px;font-weight:700;color:var(--muted)}
.site-footer .copy{position:absolute;left:0;top:14px}
.site-footer .contact{position:absolute;right:9px;top:14px}
</style>
</head>
<body>
<header class="site-header">
  <div class="brand">QUORVATRADE</div>
  <div class="auth-btn register">REGISTER</div>
  <div class="auth-btn login">LOG IN</div>
</header>
<div class="ticker">
  <span style="left:30px">Last: N/A</span>
  <span style="left:141px">Low: 2</span>
  <span style="left:240px">High: 109863</span>
  <span style="left:378px">VWAP: 108663</span>
  <span style="left:528px">Bid: 0</span>
  <span style="left:615px">Ask: 108663</span>
  <div class="chat-badge" role="img" aria-label="Live chat"></div>
</div>

<section class="chart-card">
<svg width="1000" height="516" viewBox="0 0 1000 516" font-family="Open Sans, sans-serif">
  <text x="498" y="20" text-anchor="middle" font-size="17" fill="#666">US$/BTC</text>
  <g font-size="8" fill="#666">
    <rect x="278" y="41" width="22" height="3" fill="var(--s1)"/><text x="304" y="45">preis ex-a</text>
    <rect x="359" y="41" width="22" height="3" fill="var(--s2)"/><text x="384" y="45">preis ex-b</text>
    <rect x="437" y="41" width="22" height="3" fill="var(--s3)"/><text x="462" y="45">preis ex-c</text>
    <rect x="510" y="41" width="22" height="3" fill="var(--s4)"/><text x="535" y="45">preis ex-d</text>
    <rect x="590" y="41" width="22" height="3" fill="var(--s5)"/><text x="615" y="45">preis ex-e</text>
    <rect x="656" y="41" width="22" height="3" fill="var(--s6)"/><text x="681" y="45">preis ex-f</text>
  </g>
  <g stroke="var(--grid)" stroke-width="1">
    <line x1="28" x2="977" y1="457" y2="457"/><line x1="28" x2="977" y1="440" y2="440"/><line x1="28" x2="977" y1="423" y2="423"/><line x1="28" x2="977" y1="406" y2="406"/><line x1="28" x2="977" y1="373" y2="373"/><line x1="28" x2="977" y1="356" y2="356"/><line x1="28" x2="977" y1="339" y2="339"/><line x1="28" x2="977" y1="322" y2="322"/><line x1="28" x2="977" y1="289" y2="289"/><line x1="28" x2="977" y1="272" y2="272"/><line x1="28" x2="977" y1="255" y2="255"/><line x1="28" x2="977" y1="238" y2="238"/><line x1="28" x2="977" y1="205" y2="205"/><line x1="28" x2="977" y1="188" y2="188"/><line x1="28" x2="977" y1="171" y2="171"/><line x1="28" x2="977" y1="154" y2="154"/><line x1="28" x2="977" y1="121" y2="121"/><line x1="28" x2="977" y1="104" y2="104"/><line x1="28" x2="977" y1="87" y2="87"/><line x1="28" x2="977" y1="70" y2="70"/>
  </g>
  <g stroke="#d4d4d4" stroke-width="1">
    <line x1="28" x2="977" y1="474" y2="474"/><line x1="28" x2="977" y1="390" y2="390"/><line x1="28" x2="977" y1="305" y2="305"/><line x1="28" x2="977" y1="221" y2="221"/><line x1="28" x2="977" y1="137" y2="137"/><line x1="28" x2="977" y1="53" y2="53"/>
  </g>
  <g font-size="8" fill="#666" text-anchor="end">
    <text x="18" y="477">0</text><text x="18" y="393">50</text><text x="18" y="308">100</text><text x="18" y="224">150</text><text x="18" y="140">200</text><text x="18" y="56">250</text>
  </g>
  <g fill="none" stroke-width="2.5" stroke-linejoin="round">
    <polyline stroke="var(--s5)" points="28,474 150,474 170,473 250,472 270,460 285,457 292,427 300,444 315,450 330,448 335,445 345,457 355,456 370,461"/>
    <polyline stroke="var(--s1)" points="28,474 150,474 170,473 250,472 270,462 285,458 292,425 300,443 315,450 330,449 335,446 345,458 355,455 370,461 400,469 420,471 460,464 500,466 600,464 630,457 645,451 660,455 700,454 750,452 780,443 800,421 815,392 822,322 830,216 835,99 840,356 846,220 852,315 860,282 870,263 880,247 890,305 900,313 908,353 915,305 930,308 945,286 955,230 965,262 977,230"/>
    <polyline stroke="var(--s2)" points="370,461 400,470 420,472 460,465 500,467 600,465 630,458 645,452 660,456 700,455 750,453 780,445 800,425 815,395 822,326 830,222 835,108 840,360 846,228 852,318 860,286 870,266 880,250 890,308 900,316 908,355 915,310 930,312 945,296 955,262 965,276 977,262"/>
    <polyline stroke="var(--s6)" points="370,461 400,469 420,471 460,464 500,466 600,464 630,457 645,451 660,455 700,454 750,452 780,443 800,421 815,391 822,322 830,218 835,95 840,362 846,218 852,312 860,280 870,262 880,246 890,302 900,310 908,356 915,308 930,312 945,292 955,254 965,268 977,258"/>
  </g>
  <g font-size="8" fill="#666" text-anchor="end">
    <text transform="translate(36,486) rotate(-45)">17/07/201...</text>
    <text transform="translate(60,486) rotate(-45)">17/08/201...</text>
    <text transform="translate(85,486) rotate(-45)">17/09/201...</text>
    <text transform="translate(109,486) rotate(-45)">17/10/201...</text>
    <text transform="translate(134,486) rotate(-45)">17/11/201...</text>
    <text transform="translate(158,486) rotate(-45)">17/12/201...</text>
    <text transform="translate(182,486) rotate(-45)">17/01/201...</text>
    <text transform="translate(207,486) rotate(-45)">17/02/201...</text>
    <text transform="translate(231,486) rotate(-45)">17/03/201...</text>
    <text transform="translate(256,486) rotate(-45)">17/04/201...</text>
    <text transform="translate(280,486) rotate(-45)">17/05/201...</text>
    <text transform="translate(304,486) rotate(-45)">17/06/201...</text>
    <text transform="translate(329,486) rotate(-45)">17/07/201...</text>
    <text transform="translate(353,486) rotate(-45)">17/08/201...</text>
    <text transform="translate(378,486) rotate(-45)">17/09/201...</text>
    <text transform="translate(402,486) rotate(-45)">17/10/201...</text>
    <text transform="translate(426,486) rotate(-45)">17/11/201...</text>
    <text transform="translate(451,486) rotate(-45)">17/12/201...</text>
    <text transform="translate(475,486) rotate(-45)">17/01/201...</text>
    <text transform="translate(500,486) rotate(-45)">17/02/201...</text>
    <text transform="translate(524,486) rotate(-45)">17/03/201...</text>
    <text transform="translate(548,486) rotate(-45)">17/04/201...</text>
    <text transform="translate(573,486) rotate(-45)">17/05/201...</text>
    <text transform="translate(597,486) rotate(-45)">17/06/201...</text>
    <text transform="translate(622,486) rotate(-45)">17/07/201...</text>
    <text transform="translate(646,486) rotate(-45)">17/08/201...</text>
    <text transform="translate(670,486) rotate(-45)">17/09/201...</text>
    <text transform="translate(695,486) rotate(-45)">17/10/201...</text>
    <text transform="translate(719,486) rotate(-45)">17/11/201...</text>
    <text transform="translate(744,486) rotate(-45)">17/12/201...</text>
    <text transform="translate(768,486) rotate(-45)">17/01/201...</text>
    <text transform="translate(792,486) rotate(-45)">17/02/201...</text>
    <text transform="translate(817,486) rotate(-45)">17/03/201...</text>
    <text transform="translate(841,486) rotate(-45)">17/04/201...</text>
    <text transform="translate(866,486) rotate(-45)">17/05/201...</text>
    <text transform="translate(890,486) rotate(-45)">17/06/201...</text>
    <text transform="translate(914,486) rotate(-45)">17/07/201...</text>
    <text transform="translate(939,486) rotate(-45)">17/08/201...</text>
    <text transform="translate(963,486) rotate(-45)">17/09/201...</text>
  </g>
</svg>
</section>

<section class="panel bids">
  <h2>BIDS</h2>
  <table style="width:270px">
    <tr><th style="width:132px">PRICE</th><th>QUANTITY</th></tr>
    <tr><td>101946</td><td>0.08</td></tr>
    <tr><td>101946</td><td>0.08</td></tr>
    <tr><td>101946</td><td>0.08</td></tr>
    <tr><td>101946</td><td>0.08</td></tr>
  </table>
</section>
<section class="panel asks">
  <h2>ASKS</h2>
  <table style="width:270px">
    <tr><th style="width:132px">PRICE</th><th>QUANTITY</th></tr>
    <tr><td>101946</td><td>0.08</td></tr>
    <tr><td>101946</td><td>0.08</td></tr>
    <tr><td>101946</td><td>0.08</td></tr>
    <tr><td>101946</td><td>0.08</td></tr>
  </table>
</section>
<section class="panel trades">
  <h2>TRADES</h2>
  <table style="width:328px">
    <tr><th style="width:122px">PRICE</th><th style="width:121px">QUANTITY</th><th>TIMESTAMP</th></tr>
    <tr><td>101946</td><td>0.08</td><td>&nbsp;2</td></tr>
    <tr><td>101946</td><td>0.08</td><td>&nbsp;2</td></tr>
    <tr><td>101946</td><td>0.08</td><td>&nbsp;2</td></tr>
    <tr><td>101946</td><td>0.08</td><td>&nbsp;2</td></tr>
  </table>
</section>

<footer class="site-footer">
  <span class="copy">Copyright © 2014 - quorvatrade.example</span>
  <span class="contact">Contact us</span>
</footer>
</body>
</html>
```